Experienced Home remodel service

I'm a home remodeler. I want a catch phrase that clearly describes viewers what kind of work I'm in like the purple phrase on my rough draft idea. I need my website, phone, logo, slogan included. The picture is of my daughter. I want her on it. Be cool if something could be added to her picture like a hard hat or tool belt ect and her picture cut out/background removed. Some kind of background other than plain white for whole picture. I added extra pics of her so pick one

Target Market(s)

Home owners between 30-60

Industry/Entity Type

Home renovation/remodel

Colors

Designer to choose colors to be used in the design.

Requirements
Must have
• Daughters picture incorporated. Logo, phone, website address, slogan,
Nice to have
• See a hardhat or tool belt added to one of my daughters pictures that is chosen to use by designer

```html
<!DOCTYPE html>
<html lang="en">
<head>
<meta charset="utf-8">
<title>Harlow Home Solutions – Billboard</title>
<link rel="stylesheet" href="https://fonts.googleapis.com/css2?family=Oswald:wght@600;700&family=Roboto+Slab:wght@400&family=Roboto:wght@700&family=Montserrat:wght@600;700;800&display=swap">
<style>
  :root {
    --page-bg: #e6e9ee;
    --ink: #111111;
    --charcoal: #23252b;
    --charcoal-soft: #33363d;
    --gold: #e0a325;
    --white: #ffffff;
    --panel-light: #ececed;
    --panel-mid: #dcdcdf;
    --photo-top: #e9d46a;
    --photo-mid: #d9b6a0;
    --photo-low: #d3c0e4;
    --photo-base: #bfa6d8;
  }
  * { margin: 0; padding: 0; box-sizing: border-box; }
  html, body { width: 1200px; height: 900px; overflow: hidden; }
  body { background: var(--page-bg); position: relative; font-family: "Montserrat", sans-serif; }

  .billboard {
    position: absolute; left: 20px; top: 167px;
    width: 1160px; height: 566px;
    background: linear-gradient(135deg, var(--panel-light), var(--panel-mid));
    overflow: hidden;
  }
  .billboard__shapes { position: absolute; inset: 0; }

  .hero-photo {
    position: absolute; left: 563px; top: 21px; width: 441px; height: 545px;
    border-radius: 200px 200px 0 0;
    background: linear-gradient(180deg, var(--photo-top) 0%, var(--photo-mid) 28%, var(--photo-low) 55%, var(--photo-base) 100%);
  }

  .headline {
    position: absolute; left: 54px; top: 32px; width: 640px;
    font-family: "Oswald", sans-serif; font-weight: 700;
    font-size: 58px; line-height: 1.1; letter-spacing: -1px;
    color: var(--gold); text-shadow: 2px 3px 3px rgba(0,0,0,.6);
    white-space: nowrap;
  }
  .slogan {
    position: absolute; left: 120px; top: 108px; width: 505px; text-align: center;
    font-family: "Roboto Slab", serif; font-size: 42px; line-height: 1.1;
    color: var(--white);
  }
  .catchphrase {
    position: absolute; left: 100px; top: 177px; width: 540px; text-align: center;
    font-family: "Roboto", sans-serif; font-weight: 700;
    font-size: 45px; line-height: 1.13; letter-spacing: -0.5px;
    color: var(--white); text-shadow: 1px 2px 3px rgba(0,0,0,.55);
  }
  .catchphrase__accent { color: var(--gold); }

  .contact { position: absolute; left: 45px; top: 412px; }
  .contact__icon { position: absolute; left: 0; top: 12px; width: 86px; height: 86px; }
  .contact__label {
    position: absolute; left: 97px; top: 0; white-space: nowrap;
    font-weight: 700; font-size: 26px; color: var(--ink);
  }
  .contact__phone {
    position: absolute; left: 95px; top: 30px; white-space: nowrap;
    font-weight: 800; font-size: 60px; letter-spacing: -1px; color: var(--gold);
  }
  .contact__web {
    position: absolute; left: 0; top: 107px; white-space: nowrap;
    font-weight: 700; font-size: 27.5px; color: var(--ink);
  }

  .brand-mark { position: absolute; left: 900px; top: 40px; width: 245px; text-align: center; }
  .brand-mark__square { width: 46px; height: 46px; background: var(--ink); margin: 40px auto 28px; }
  .brand-mark__name {
    font-family: "Montserrat", sans-serif; font-weight: 800; font-size: 17px;
    line-height: 1; letter-spacing: 1.5px; color: var(--ink); text-transform: uppercase;
  }
  .brand-mark__tagline {
    margin-top: 12px; font-weight: 600; font-size: 11px; letter-spacing: 3px; color: var(--ink);
  }
  .brand-mark__phone {
    margin-top: 2px; font-weight: 600; font-size: 11px; letter-spacing: 2.5px; color: var(--ink);
  }

  .social { position: absolute; left: 987px; top: 504px; display: flex; gap: 10px; }
  .social__dot { width: 38px; height: 38px; border-radius: 50%; background: var(--ink); }
</style>
</head>
<body>
  <main class="billboard">
    <svg class="billboard__shapes" width="1160" height="566" viewBox="0 0 1160 566" aria-hidden="true">
      <defs>
        <linearGradient id="darkPanel" x1="0" y1="0" x2="1" y2="1">
          <stop offset="0" stop-color="var(--charcoal-soft)"/>
          <stop offset="1" stop-color="var(--charcoal)"/>
        </linearGradient>
      </defs>
      <path class="gold-swoosh" d="M0 240 Q300 430 598 342 L594 356 Q300 456 0 282 Z" fill="#e0a325"/>
      <path class="dark-panel" d="M0 0 L922 0 L598 342 Q300 428 0 234 Z" fill="url(#darkPanel)"/>
      <line class="gold-edge" x1="922" y1="2" x2="860" y2="120" stroke="#e0a325" stroke-width="2"/>
    </svg>
    <div class="dark-panel-photo" role="img" aria-label="Dimmed photo of a modern two-storey house behind the headline" style="position:absolute;left:0;top:0;width:1px;height:1px;"></div>

    <div class="hero-photo" role="img" aria-label="Cut-out photo of the owner's smiling daughter in a yellow hard hat and lilac puffer jacket, holding a hammer"></div>

    <h1 class="headline">HARLOW HOME SOLUTIONS</h1>
    <p class="slogan">Build - Repair - Replace</p>
    <p class="catchphrase">FOR ALL<br>YOUR <span class="catchphrase__accent">HOME REMODEL</span><br>NEEDS</p>

    <div class="contact">
      <svg class="contact__icon" viewBox="0 0 100 100" aria-hidden="true">
        <path d="M22 12 C14 14 8 22 10 34 C14 58 40 86 66 90 C78 92 86 86 88 78 L74 64 C70 60 66 62 62 66 L58 70 C46 64 36 54 30 42 L34 38 C38 34 40 30 36 26 Z" fill="#111"/>
        <path d="M54 28 A20 20 0 0 1 72 46" fill="none" stroke="#111" stroke-width="5" stroke-linecap="round"/>
        <path d="M56 14 A34 34 0 0 1 86 44" fill="none" stroke="#111" stroke-width="5" stroke-linecap="round"/>
      </svg>
      <p class="contact__label">CALL US TODAY :</p>
      <p class="contact__phone">555-014-2280</p>
      <p class="contact__web">www.harlowhomesolutions.com</p>
    </div>

    <div class="brand-mark">
      <div class="brand-mark__square"></div>
      <p class="brand-mark__name">Harlow Home<br>Solutions</p>
      <p class="brand-mark__tagline">BUILD. REPAIR. REPLACE.</p>
      <p class="brand-mark__phone">(555) 014 2280</p>
    </div>

    <div class="social" aria-label="Social media links">
      <span class="social__dot"></span>
      <span class="social__dot"></span>
      <span class="social__dot"></span>
    </div>
  </main>
</body>
</html>
```